The Jawline Remedy Business Card

Looking for a business card design: front and back. It will be printed at presspanda.example on a leaf cutout trifecta paper with green middle. 3.5 x 2 leaf cutout. It will need bleed room around edges. The front will have my picture, logo, website and email address. The back will be a quote. "Finally. The complete solution to helping you open your mouth fully without pain"
and
"Like Us on Chatterbox to Learn More @ The Jawline Remedy"

Target Market(s)

Women 20-55 years old

Industry/Entity Type

Health Service

Contact Information for Business Card

My photo on one side or embedded, Name: Dr. Marlon Quaid, PT, DPT, MS Website: TheJawlineRemedy.example Email: marlon@keystonemotionclinic.example

Requirements
Must have
• Unique design consistent with my logo

```html
<!DOCTYPE html>
<html lang="en">
<head>
<meta charset="utf-8">
<title>The Jawline Remedy – Business Card</title>
<link href="https://fonts.googleapis.com/css2?family=Josefin+Sans:wght@300;400;600;700&display=swap" rel="stylesheet">
<style>
  :root {
    --brand-blue: #1b6cb0;
    --brand-green: #7dbb35;
    --card-white: #f3f3f3;
    --backdrop: #e6e6e6;
    --text-blue: #2a68ad;
    --photo-dark: #4a4540;
    --photo-light: #8a8378;
  }
  * { box-sizing: border-box; margin: 0; padding: 0; }
  html, body { width: 1200px; height: 1200px; overflow: hidden; }
  body {
    background: var(--backdrop);
    font-family: "Josefin Sans", sans-serif;
    position: relative;
  }
  .card {
    position: absolute;
    left: 227px;
    width: 745px;
    height: 425px;
    border-radius: 38px;
    overflow: hidden;
  }
  /* Front */
  .card-front { top: 135px; background: var(--card-white); }
  .side-band {
    position: absolute; left: 0; top: 0; bottom: 0; width: 143px;
    background: var(--brand-blue);
  }
  .side-rule {
    position: absolute; left: 144px; top: 0; bottom: 0; width: 4px;
    background: var(--brand-green);
  }
  .portrait {
    position: absolute; left: 63px; top: 113px;
    width: 200px; height: 200px; border-radius: 50%;
    border: 3px solid #ffffff;
    background: radial-gradient(circle at 50% 40%, var(--photo-light), var(--photo-dark));
  }
  .brand-front {
    position: absolute; left: 360px; top: 48px; height: 132px;
    display: flex; align-items: center; gap: 18px;
  }
  .brand-mark {
    width: 128px; height: 128px; border-radius: 50%;
    border: 4px solid var(--brand-blue);
  }
  .brand-name {
    font-weight: 700; font-size: 32px; line-height: 38px;
    color: var(--brand-green);
  }
  .person { position: absolute; left: 359px; top: 247px; }
  .person-name { font-weight: 600; font-size: 26px; color: var(--brand-green); }
  .person-creds { font-weight: 300; font-size: 21px; color: var(--text-blue); margin-top: 6px; }
  .contact-list { position: absolute; left: 360px; top: 327px; list-style: none; }
  .contact-item {
    display: flex; align-items: center; gap: 10px;
    font-weight: 300; font-size: 19px; color: var(--text-blue);
    height: 28px;
  }
  .contact-icon { width: 18px; height: 18px; flex: none; }
  /* Back */
  .card-back { top: 638px; background: var(--brand-blue); }
  .back-invite {
    position: absolute; top: 40px; left: 0; right: 0; text-align: center;
    font-weight: 300; font-size: 19px; color: #ffffff;
  }
  .back-invite .handle { color: var(--brand-green); }
  .brand-back {
    position: absolute; left: 170px; top: 115px; height: 180px;
    display: flex; align-items: center; gap: 22px;
  }
  .brand-back .brand-mark { width: 176px; height: 176px; border-color: #ffffff; }
  .brand-back .brand-name { font-size: 46px; line-height: 54px; }
  .tagline-band {
    position: absolute; left: 0; right: 0; top: 352px; height: 40px;
    background: var(--brand-green);
    display: flex; align-items: center; justify-content: center;
    font-weight: 300; font-size: 18px; color: #ffffff; padding-top: 3px;
  }
</style>
</head>
<body>
  <section class="card card-front">
    <div class="side-band"></div>
    <div class="side-rule"></div>
    <div class="portrait" role="img" aria-label="Portrait photo of Dr. Marlon Quaid"></div>
    <div class="brand-front">
      <div class="brand-mark"></div>
      <div class="brand-name">The<br>Jawline<br>Remedy</div>
    </div>
    <div class="person">
      <div class="person-name">Dr. Marlon Quaid</div>
      <div class="person-creds">PT, DPT, MS</div>
    </div>
    <ul class="contact-list">
      <li class="contact-item">
        <svg class="contact-icon" viewBox="0 0 18 18">
          <circle cx="9" cy="9" r="9" fill="#7dbb35"/>
          <rect x="4" y="5.5" width="10" height="7" fill="none" stroke="#fff" stroke-width="1.2"/>
          <path d="M4 5.5 L9 9.5 L14 5.5" fill="none" stroke="#fff" stroke-width="1.2"/>
        </svg>
        marlon@keystonemotionclinic.example
      </li>
      <li class="contact-item">
        <svg class="contact-icon" viewBox="0 0 18 18">
          <circle cx="9" cy="9" r="9" fill="#7dbb35"/>
          <circle cx="9" cy="9" r="5" fill="none" stroke="#fff" stroke-width="1.2"/>
          <path d="M4 9 H14 M9 4 C6.5 6.5 6.5 11.5 9 14 M9 4 C11.5 6.5 11.5 11.5 9 14" fill="none" stroke="#fff" stroke-width="1"/>
        </svg>
        www.TheJawlineRemedy.example
      </li>
    </ul>
  </section>

  <section class="card card-back">
    <p class="back-invite">Like Us on Chatterbox to Learn More <span class="handle">@ The Jawline Remedy</span></p>
    <div class="brand-back">
      <div class="brand-mark"></div>
      <div class="brand-name">The<br>Jawline<br>Remedy</div>
    </div>
    <div class="tagline-band">Finally. The complete solution to helping you open your mouth fully without pain</div>
  </section>
</body>
</html>
```